Business Cards for wirefen.com.au
Logo already designed by Quillnoxa
Professional
Liam Forbury
Technical Engineer
Mobile: 0437 125 806
liam@wirefen.com.au
www.wirefen.com.au
Should have the text: "Cloud Application Development"

```html
<!DOCTYPE html>
<html lang="en">
<head>
<meta charset="utf-8">
<title>wirefen.com.au — Business Cards</title>
<link href="https://fonts.googleapis.com/css2?family=Arimo:wght@400;700&family=Tinos&display=swap" rel="stylesheet">
<style>
  :root {
    --backdrop: #dcd8d3;
    --card: #ffffff;
    --card-edge: #f2f2f2;
    --brand-blue: #2f6cb5;
    --brand-ink: #1f2f4a;
    --tagline: #6b7480;
    --text: #222222;
    --watermark: #f0f0f0;
  }
  * { margin: 0; padding: 0; box-sizing: border-box; }
  html, body { width: 1200px; height: 763px; overflow: hidden; background: var(--backdrop); }
  .canvas { position: relative; width: 1200px; height: 763px; }

  .card {
    position: absolute;
    width: 523px; height: 298px;
    border-radius: 16px;
    background: linear-gradient(180deg, var(--card) 0%, var(--card-edge) 100%);
    box-shadow: 0 4px 12px rgba(0,0,0,0.18);
    overflow: hidden;
  }
  .card--front-a { left: 67px;  top: 67px; }
  .card--back-a  { left: 612px; top: 67px; }
  .card--front-b { left: 67px;  top: 408px; }
  .card--back-b  { left: 612px; top: 408px; }

  .mark-dot { position: absolute; border-radius: 50%; background: var(--brand-blue); }
  .watermark-dot { position: absolute; border-radius: 50%; background: var(--watermark); }

  .brand-name {
    position: absolute;
    font-family: "Arimo", Arial, sans-serif;
    font-weight: 700;
    color: var(--brand-ink);
    line-height: 1;
    white-space: nowrap;
  }
  .tagline {
    position: absolute;
    font-family: "Arimo", Arial, sans-serif;
    font-style: italic;
    color: var(--tagline);
    line-height: 1;
    white-space: nowrap;
  }
  .person { position: absolute; font-family: "Tinos", "Times New Roman", serif; color: var(--text); line-height: 1; }
  .person__name { font-size: 24px; letter-spacing: 1px; }
  .person__role { font-size: 17px; margin-top: 6px; }

  .contacts { position: absolute; list-style: none; font-family: "Arimo", Arial, sans-serif; font-size: 15px; color: var(--text); }
  .contacts li { display: flex; align-items: center; height: 24px; }
  .contacts svg { width: 15px; height: 15px; margin-right: 8px; flex: none; }
  .centered { text-align: center; left: 0; right: 0; }
</style>
</head>
<body>
<main class="canvas">

  <!-- Front, layout A -->
  <section class="card card--front-a">
    <div class="watermark-dot" style="left:239px; top:11px; width:300px; height:300px;"></div>
    <div class="mark-dot" style="left:60px; top:36px; width:106px; height:106px;"></div>
    <div class="brand-name" style="left:29px; top:148px; font-size:22px;">wirefen.com.au</div>
    <div class="tagline" style="left:30px; top:177px; font-size:10px;">"Cloud Application Development"</div>
    <div class="person" style="left:305px; top:18px;">
      <div class="person__name">Liam Forbury</div>
      <div class="person__role">Technical Engineer</div>
    </div>
    <ul class="contacts" style="left:315px; top:196px;">
      <li><svg viewBox="0 0 16 16"><rect x="4" y="1" width="8" height="14" rx="1.5" fill="none" stroke="#222" stroke-width="1.5"/><circle cx="8" cy="12.5" r="1" fill="#222"/></svg>0437 125 806</li>
      <li><svg viewBox="0 0 16 16"><circle cx="8" cy="8" r="2.8" fill="none" stroke="#222" stroke-width="1.6"/><path d="M10.8 5.5v3.6c0 1.6 2.6 1.6 2.6-.6A5.4 5.4 0 1 0 11 13" fill="none" stroke="#222" stroke-width="1.6"/></svg>liam@wirefen.com.au</li>
      <li><svg viewBox="0 0 16 16"><circle cx="8" cy="8" r="6.5" fill="none" stroke="#222" stroke-width="1.4"/><ellipse cx="8" cy="8" rx="2.8" ry="6.5" fill="none" stroke="#222" stroke-width="1.2"/><line x1="1.5" y1="8" x2="14.5" y2="8" stroke="#222" stroke-width="1.2"/></svg>www.wirefen.com.au</li>
    </ul>
  </section>

  <!-- Back, layout A -->
  <section class="card card--back-a">
    <div class="mark-dot" style="left:191px; top:43px; width:140px; height:140px;"></div>
    <div class="brand-name centered" style="top:202px; font-size:32px;">wirefen.com.au</div>
    <div class="tagline centered" style="top:242px; font-size:12px;">"Cloud Application Development"</div>
  </section>

  <!-- Front, layout B -->
  <section class="card card--front-b">
    <div class="mark-dot" style="left:93px; top:21px; width:160px; height:160px;"></div>
    <div class="brand-name" style="left:37px; top:200px; font-size:36px;">wirefen.com.au</div>
    <div class="tagline" style="left:40px; top:248px; font-size:12px;">"Cloud Application Development"</div>
    <div class="person" style="left:346px; top:24px;">
      <div class="person__name">Liam Forbury</div>
      <div class="person__role">Technical Engineer</div>
    </div>
    <ul class="contacts" style="left:336px; top:112px;">
      <li><svg viewBox="0 0 16 16"><rect x="4" y="1" width="8" height="14" rx="1.5" fill="none" stroke="#222" stroke-width="1.5"/><circle cx="8" cy="12.5" r="1" fill="#222"/></svg>0437 125 806</li>
      <li><svg viewBox="0 0 16 16"><circle cx="8" cy="8" r="2.8" fill="none" stroke="#222" stroke-width="1.6"/><path d="M10.8 5.5v3.6c0 1.6 2.6 1.6 2.6-.6A5.4 5.4 0 1 0 11 13" fill="none" stroke="#222" stroke-width="1.6"/></svg>liam@wirefen.com.au</li>
      <li><svg viewBox="0 0 16 16"><circle cx="8" cy="8" r="6.5" fill="none" stroke="#222" stroke-width="1.4"/><ellipse cx="8" cy="8" rx="2.8" ry="6.5" fill="none" stroke="#222" stroke-width="1.2"/><line x1="1.5" y1="8" x2="14.5" y2="8" stroke="#222" stroke-width="1.2"/></svg>www.wirefen.com.au</li>
    </ul>
  </section>

  <!-- Back, layout B -->
  <section class="card card--back-b">
    <div class="watermark-dot" style="left:212px; top:40px; width:240px; height:240px;"></div>
    <div class="mark-dot" style="left:72px; top:80px; width:84px; height:84px;"></div>
    <div class="brand-name" style="left:46px; top:178px; font-size:20px;">wirefen.com.au</div>
    <div class="tagline" style="left:50px; top:206px; font-size:8px;">"Cloud Application Development"</div>
  </section>

</main>
</body>
</html>
```